Corrowin Sack operates across the US and Australasia providing calico bags to small business through to large enterprise across all verticals. Our bags are the most premium in the market place and our customer service is second to none. Our competitive advantage lays in our competitive pricing, superior quality and outstanding customer service.

Industry/Entity Type

Business

Contact Information for Business Card

Corrowin Sack
Marisol Quenby
Managing Director
marisol@corrowinsack.com
www.corrowinsack.com.au
Mobile:- 0471 896 305
Level 3, 284 Harwick Street
Melbourne Victoria Australia 3000

```html
<!DOCTYPE html>
<html lang="en">
<head>
<meta charset="utf-8">
<title>Corrowin Sack – Business Card</title>
<link rel="stylesheet" href="https://fonts.googleapis.com/css2?family=Arimo:wght@400;700&family=Playfair+Display:wght@400&display=swap">
<style>
  :root {
    --backdrop: #e9e7e3;
    --card: #ffffff;
    --ink: #0b0b0b;
    --leaf: #5fbf2e;
    --leaf-light: #a6dc6e;
    --leaf-deep: #3f9a1c;
    --signal: #d2232a;
    --paper-text: #ffffff;
  }
  * { margin: 0; padding: 0; box-sizing: border-box; }
  html, body {
    width: 1200px; height: 892px; overflow: hidden;
    background: var(--backdrop);
    font-family: "Arimo", Arial, sans-serif;
  }
  .canvas {
    position: relative; width: 1200px; height: 892px;
  }
  .card {
    position: absolute; top: 291px;
    width: 540px; height: 309px;
    background: var(--card);
    box-shadow: 0 6px 18px rgba(0,0,0,.18);
    overflow: hidden;
  }
  .card--back { left: 40px; }
  .card--front { left: 620px; }

  /* Back side */
  .map-area {
    position: absolute;
    background: radial-gradient(ellipse at 45% 40%, var(--leaf-light), var(--leaf) 60%, var(--leaf-deep));
    border-radius: 38% 46% 42% 50% / 44% 40% 52% 46%;
  }
  .card--back .map-area { left: 150px; top: 40px; width: 240px; height: 210px; }
  .brand-name {
    position: absolute;
    font-family: "Arimo", Arial, sans-serif;
    font-weight: 700;
    color: var(--ink);
    letter-spacing: .04em;
    white-space: nowrap;
    display: flex; align-items: center; gap: 8px;
  }
  .brand-name .brand-dot {
    width: 12px; height: 12px; border-radius: 50%;
    background: var(--signal);
  }
  .card--back .brand-name { left: 50%; top: 130px; transform: translateX(-50%); font-size: 30px; }

  /* Front side */
  .side-tab {
    position: absolute; left: 14px; top: 22px;
    width: 30px; height: 200px;
    background: var(--ink); border-radius: 9px;
  }
  .card--front .map-area { left: 150px; top: 36px; width: 150px; height: 130px; }
  .card--front .brand-name { left: 225px; top: 90px; transform: translateX(-50%); font-size: 18px; gap: 6px; }
  .card--front .brand-name .brand-dot { width: 9px; height: 9px; }

  .contact-panel {
    position: absolute; left: 300px; top: 150px;
    width: 260px; height: 138px;
    background: var(--ink);
    border-radius: 12px 0 0 12px;
    padding: 12px 0 0 22px;
    color: var(--paper-text);
  }
  .person-name {
    font-family: "Playfair Display", Georgia, serif;
    font-size: 26px; color: var(--leaf); line-height: 1.05;
  }
  .person-role { font-size: 13px; margin: 2px 0 10px; }
  .contact-list { list-style: none; font-size: 12px; line-height: 1.55; }
  .contact-list li { display: flex; align-items: center; gap: 8px; }
  .contact-icon {
    width: 11px; height: 11px; background: var(--signal);
    border-radius: 2px; display: inline-flex; align-items: center; justify-content: center;
    flex: none;
  }
  .address {
    position: absolute; left: 20px; bottom: 8px;
    font-size: 12px; color: var(--signal); white-space: nowrap;
  }
</style>
</head>
<body>
<main class="canvas">

  <section class="card card--back" aria-label="Card back">
    <div class="map-area" role="img" aria-label="Green map of Australia behind the company name"></div>
    <div class="brand-name"><span class="brand-dot"></span>Corrowin Sack</div>
  </section>

  <section class="card card--front" aria-label="Card front">
    <div class="side-tab"></div>
    <div class="map-area" role="img" aria-label="Green map of Australia behind the company name"></div>
    <div class="brand-name"><span class="brand-dot"></span>Corrowin Sack</div>

    <div class="contact-panel">
      <h1 class="person-name">Marisol Quenby</h1>
      <p class="person-role">Managing Director</p>
      <ul class="contact-list">
        <li><span class="contact-icon"><svg width="7" height="7" viewBox="0 0 10 10"><path d="M2 1l2 2-1 1.5c.6 1.2 1.4 2 2.5 2.5L7 6l2 2-1.5 1.5C4 9 1 6 .5 2.5z" fill="#fff"/></svg></span>0471 896 305</li>
        <li><span class="contact-icon"><svg width="7" height="7" viewBox="0 0 10 10"><rect x="1" y="2" width="8" height="6" fill="none" stroke="#fff" stroke-width="1.2"/><path d="M1 2l4 3.5L9 2" fill="none" stroke="#fff" stroke-width="1.2"/></svg></span>marisol@corrowinsack.com</li>
        <li><span class="contact-icon"><svg width="7" height="7" viewBox="0 0 10 10"><circle cx="5" cy="5" r="4" fill="none" stroke="#fff" stroke-width="1.2"/><path d="M1 5h8M5 1c2 2.5 2 5.5 0 8M5 1c-2 2.5-2 5.5 0 8" fill="none" stroke="#fff" stroke-width=".8"/></svg></span>www.corrowinsack.com.au</li>
      </ul>
    </div>

    <p class="address">Level 3, 284 Harwick Street Melbourne Victoria Australia 3000</p>
  </section>

</main>
</body>
</html>
```